New business card for civil engineering company - "Keystone Audit"

We need a business card designed for our new structural engineering company.

The company name is "Keystone Audit" logo files attached.

We would like the following:
* Two-sided card
* Simple design

Information to be placed on the card:
Name - Marcus Dellow
Job Title - Director / Structural Engineer
Credentials - BEng(Hons), CPEng, CMengNZ, IntPE(NZ)
Email - marcus.dellow@keystoneaudit.co.nz
mobile - 0219364058
website - www.keystoneaudit.co.nz

```html
<!DOCTYPE html>
<html lang="en">
<head>
<meta charset="utf-8">
<title>Keystone Audit — Business Card</title>
<link href="https://fonts.googleapis.com/css2?family=Rubik:wght@400;500;600&display=swap" rel="stylesheet">
<style>
  :root {
    --backdrop: #1c1c1e;
    --front-top: #2d5b8e;
    --front-bottom: #234a7a;
    --back-paper: #f2f2f1;
    --ink-dark: #353535;
    --ink-muted: #7a7a7a;
    --ink-blue: #2a4f7e;
    --ink-light: #ffffff;
    --tag-light: #d6e2ef;
  }
  * { margin: 0; padding: 0; box-sizing: border-box; }
  html, body {
    width: 1200px; height: 900px; overflow: hidden;
    background: var(--backdrop);
    font-family: "Rubik", Arial, sans-serif;
  }
  .canvas {
    position: relative; width: 1200px; height: 900px;
  }
  .card {
    position: absolute; left: 270px; width: 660px; height: 367px;
    box-shadow: 0 12px 30px rgba(0,0,0,0.55);
  }
  .card--front {
    top: 58px;
    background: linear-gradient(180deg, var(--front-top) 0%, var(--front-bottom) 100%);
    display: flex; flex-direction: column; align-items: center; justify-content: center;
  }
  .card--back {
    top: 475px;
    background: var(--back-paper);
  }
  .wordmark {
    font-weight: 500; text-transform: uppercase;
    letter-spacing: 3px; font-size: 29px; line-height: 1;
  }
  .tagline {
    text-transform: uppercase; letter-spacing: 2.6px;
    font-size: 11px; margin-top: 9px;
  }
  .card--front .wordmark { color: var(--ink-light); margin-top: 150px; }
  .card--front .tagline { color: var(--tag-light); }

  .brand-block {
    position: absolute; left: 52px; top: 256px;
  }
  .brand-block .wordmark { color: var(--ink-dark); font-size: 25px; letter-spacing: 2.5px; }
  .brand-block .tagline { color: var(--ink-muted); font-size: 10px; letter-spacing: 2.2px; margin-top: 8px; }

  .contact {
    position: absolute; left: 292px; top: 58px;
    color: var(--ink-dark); font-size: 17px; line-height: 22px;
  }
  .contact__name {
    color: var(--ink-blue); font-size: 22px; font-weight: 400;
    text-transform: uppercase; letter-spacing: 0.5px; margin-bottom: 6px;
  }
  .contact__rule {
    width: 90px; height: 2px; background: var(--ink-blue);
    margin: 12px 0 50px;
  }
  .contact__web { margin-top: 46px; }
  .contact__web strong { color: var(--ink-blue); font-weight: 600; }
</style>
</head>
<body>
<main class="canvas">
  <section class="card card--front" aria-label="Card front">
    <div class="wordmark">Keystone Audit</div>
    <div class="tagline">Peer Review Specialists</div>
  </section>

  <section class="card card--back" aria-label="Card back">
    <div class="brand-block">
      <div class="wordmark">Keystone Audit</div>
      <div class="tagline">Peer Review Specialists</div>
    </div>
    <div class="contact">
      <h1 class="contact__name">Marcus Dellow</h1>
      <p>Director / Structural Engineer</p>
      <p>BEng(Hons), CPEng, CMengNZ, IntPE(NZ)</p>
      <div class="contact__rule"></div>
      <p>0219364058</p>
      <p>marcus.dellow@keystoneaudit.co.nz</p>
      <p class="contact__web">www.<strong>KEYSTONEAUDIT</strong>.co.nz</p>
    </div>
  </section>
</main>
</body>
</html>
```